Brochure Design Project

We require a brochure design for ongoing marketing of our business / services.

Purpose - As a handout to support / summarise discussions when dealing with prospective clients face to face.

Aim - Should "sell" our business , summarise our capabilities & business focus. Assist in convincing clients that we are the best solution to their logistic needs.

Brochure size - A4 (ie printed on A3 double sided & folded)
Brochure finish - Glossy, colour , medium weight ( approx 140 gsm)

Suggested Content -
Front page - Profile / Intro to company
Centre pages - Capabilities / selling points
Rear page - Depot location map, contact details, reference to website

Should be brief on words, dot points ????
Insert some colour photos.

Reference Material -
Web site (www.ferncastlegroup.com.au)
Powerpoint presentation
business unit profiles ( Word Docs.)
Draft of brochure ( too many words , no photo's !!)

Industry/Entity Type

Marketing

```html
<!DOCTYPE html>
<html lang="en">
<head>
<meta charset="utf-8">
<title>Ferncastle Group – Brochure</title>
<link href="https://fonts.googleapis.com/css2?family=Crimson+Pro:ital,wght@1,500;1,600&family=Open+Sans:ital,wght@0,400;0,600;0,700;1,400&family=Roboto+Condensed:wght@700&display=swap" rel="stylesheet">
<style>
  :root{
    --stage:#3b3b3d;
    --maroon:#7b0000;
    --red:#e3161d;
    --deep-red:#a00000;
    --charcoal:#38383a;
    --stone-1:#efece6;
    --stone-2:#d8d3ca;
    --cream:#f2e7a0;
    --pale-yellow:#f4e58a;
    --white:#ffffff;
    --ink:#333333;
  }
  *{box-sizing:border-box;margin:0;padding:0}
  html,body{width:1200px;height:872px;overflow:hidden;background:var(--stage)}
  .board{position:relative;width:1200px;height:872px;background:var(--stage);font-family:"Open Sans",Arial,sans-serif}
  .side-label{position:absolute;top:8px;font-family:"Crimson Pro",Georgia,serif;font-style:italic;font-weight:600;font-size:33px;color:var(--white)}
  .side-label--back{left:255px}
  .side-label--front{left:756px}

  .panel{position:absolute;top:62px;height:750px;overflow:hidden;box-shadow:4px 6px 10px rgba(0,0,0,.5)}
  .panel svg.panel-art{position:absolute;inset:0}
  .panel--back{left:62px;width:528px;background:var(--maroon)}
  .panel--front{left:592px;width:530px;background:linear-gradient(135deg,var(--stone-1),var(--stone-2) 60%,var(--stone-1))}

  .badge{position:absolute;left:340px;top:29px;width:106px;height:50px;background:var(--white);border:1px solid #bbb}
  .badge::after{content:"";position:absolute;right:10px;top:8px;width:34px;height:34px;border-radius:50%;background:var(--red)}

  .brand-back{position:absolute;left:270px;top:498px;font-weight:700;font-size:19px;color:var(--white);letter-spacing:.3px}
  .web-back{position:absolute;left:268px;top:535px;font-size:12.5px;font-weight:600;color:var(--pale-yellow);letter-spacing:1.6px}
  .commitment{position:absolute;left:26px;top:552px;font-family:"Crimson Pro",Georgia,serif;font-style:italic;font-weight:500;font-size:23px;line-height:30.5px;color:var(--cream)}
  .call{position:absolute;left:270px;top:577px;font-family:"Roboto Condensed",Arial,sans-serif;font-weight:700;font-size:29px;color:var(--white)}
  .address{position:absolute;right:32px;top:620px;text-align:right;font-size:10.5px;line-height:17.5px;color:var(--white)}
  .contact{position:absolute;left:24px;top:700px;font-size:14px;color:var(--white)}
  .contact em{font-style:italic}
  .contact strong{font-weight:700}
  .contact-web{position:absolute;left:24px;top:719px;font-size:13px;color:var(--white);font-weight:700;letter-spacing:.2px}
  .contact-web em{font-weight:400;font-size:11px}

  .brand-front{position:absolute;left:0;right:0;top:100px;text-align:center;font-weight:700;font-size:33px;color:var(--deep-red);letter-spacing:.6px}
  .brand-front::first-letter{color:var(--red)}
  .headline{position:absolute;left:0;right:0;top:164px;text-align:center;font-family:"Roboto Condensed",Arial,sans-serif;font-weight:700;font-size:35px;color:#3a3a3a}
  .tagline{position:absolute;left:0;right:0;top:214px;text-align:center;font-size:15px;color:var(--red)}
  .services{position:absolute;right:30px;top:312px;text-align:right;font-family:"Crimson Pro",Georgia,serif;font-style:italic;font-weight:500;font-size:25px;line-height:33px;color:var(--pale-yellow)}
  .overview-tab{position:absolute;right:0;top:504px;width:175px;height:26px;background:var(--red);border-radius:13px 0 0 13px;text-align:right;padding-right:30px;font-family:"Crimson Pro",Georgia,serif;font-style:italic;font-weight:500;font-size:22px;line-height:26px;color:var(--white)}
  .overview-body{position:absolute;right:30px;top:555px;width:470px;text-align:right;font-style:italic;font-size:7.4px;line-height:11px;color:var(--white)}
  .overview-body p{margin-bottom:8px}
</style>
</head>
<body>
<div class="board">
  <div class="side-label side-label--back">Back side</div>
  <div class="side-label side-label--front">Front side</div>

  <section class="panel panel--back">
    <svg class="panel-art" width="528" height="750" viewBox="0 0 528 750">
      <defs>
        <linearGradient id="siteTone" x1="0" y1="0" x2="0" y2="1">
          <stop offset="0" stop-color="#a9c3d6"/>
          <stop offset=".45" stop-color="#8f9aa0"/>
          <stop offset="1" stop-color="#5d6266"/>
        </linearGradient>
      </defs>
      <path d="M510 0 H528 V40 C470 300 300 470 0 560 V540 C300 470 480 300 510 0Z" fill="var(--red)"/>
      <path d="M498 0 H512 C480 300 300 470 0 540 V532 C300 460 468 300 498 0Z" fill="var(--charcoal)"/>
      <g role="img" aria-label="Photo of a grain terminal with silos and a truck on the weighbridge">
        <path d="M0 0 H498 C468 300 300 460 0 525Z" fill="url(#siteTone)"/>
      </g>
    </svg>
    <div class="badge" role="img" aria-label="Safety accreditation badge"></div>
    <div class="brand-back">Ferncastle Group</div>
    <div class="web-back">www.ferncastlegroup.com.au</div>
    <div class="commitment">Committment to<br>Safety<br>Environment<br>Community</div>
    <div class="call">Call: (02) 4000 1234</div>
    <div class="address">18 Harbourside Drive, Portview, NSW 2300<br>PO Box 412, Portview Mail Centre, NSW 2301<br>Ph: (02) 4000 1234,&nbsp;&nbsp;&nbsp;Fax: (02) 4000 1235</div>
    <div class="contact"><em>Contact Us</em> <strong>(Ferncastle Group' Logistics Team)</strong></div>
    <div class="contact-web"><em>Visit our Website:</em> http://www.ferncastlegroup.com.au/contact_us.htm</div>
  </section>

  <section class="panel panel--front">
    <svg class="panel-art" width="530" height="750" viewBox="0 0 530 750">
      <path d="M0 750 C40 470 230 250 530 236 V258 C260 270 70 470 6 750Z" fill="var(--maroon)"/>
      <path d="M8 750 C70 480 250 275 530 258 V282 C290 292 100 490 20 750Z" fill="var(--red)"/>
      <path d="M20 750 C100 500 290 300 530 282 V750Z" fill="var(--charcoal)"/>
    </svg>
    <div class="brand-front">Ferncastle Group</div>
    <div class="headline">for all logistic solution</div>
    <div class="tagline">....efficiently, timely &amp; safely</div>
    <div class="services">Transport<br>Distribution<br>Warehousing<br>Grain Handling<br>Intermodal Services</div>
    <div class="overview-tab">Overview</div>
    <div class="overview-body">
      <p>Ferncastle Group Pty Ltd is a diverse, dynamic,<br>and rapidly growing Transport &amp; Logistic company.</p>
      <p>Headquartered in Newcastle, and with a number of depots throughout<br>New South Wales &amp; Queensland, Ferncastle Group is able to provide the<br>complete logistic solution to customers throughout eastern Australia<br>Ferncastle Group today consists of a number of divisions including,<br>Transport, Intermodal, Rural &amp; Industrial services.</p>
      <p>In all of these businesses Ferncastle Group is committed to the delivery of high<br>quality service with a strong customer focus, underpinned by an overriding commitment to safety, the Chain of<br>Responsibility legislation, and working with our customers to continually refine and improve service efficiencies.</p>
      <p>The Ferncastle Group team prides itself in working with clients to provide a transport partnership that delivers<br>complete logistic solutions which encompass efficiency, value, compliance &amp; a service focussed attitude.</p>
    </div>
  </section>
</div>
</body>
</html>
```